Company Business Card Design Project - Revamp the image of an old construction company.

We need a business card designed for a new company in Australia.

Type of business is Commercial Roofing & Painting.

Medium will be brushed black metal card that can/will be acid etched to a brushed steel silver, acid die cut and two printed colours of our choice which will be white and pantone orange.

We have hopes that the design will be simple, modern and represent with a quick glance what our company does.

Please read instructions carefully in must have box any questions please ask.

If you are interested in this job please look at other job that we have which is very similar with logo and design

Please have a look at the things that can be done with metals cards on yondle images for inspiration.

Target Market(s)

Business owners, commercial property development Men from 25-70 years of age.

Industry/Entity Type

Construction

Requirements
Must have
• Front of card:

Must use the company logo and name provided as attachment (see below kestrel mark construction_black_background).

the words -Commercial Painting and Roofing- must be on front of card

details needed on front or back depending on your design

Name
position
email
mobile

all details can be on front with a cool design to be etched on the back of card or to keep front simple you can put all detail on back of card, I will leave the lay out to you.

Colours in logo are

Pantone 144 C Orange
Pantone 11-0601 White
Pantone 7539 C Gray
Pantone 426 C Black

However black will be the base of black metal card. Gray will be replaced with the etching in card revealing the silver. Orange and white will be printed on card.

Please have fun!!
Should not have
• Please don't clutter the card
No fonts smaller then 7 points

```html
<!DOCTYPE html>
<html lang="en">
<head>
<meta charset="utf-8">
<title>Kestrel Mark Construction – Business Card</title>
<link rel="stylesheet" href="https://fonts.googleapis.com/css2?family=Arimo:wght@400;700&display=swap">
<style>
  :root {
    --canvas-bg: #d9d9d9;
    --card-black: #060707;
    --orange: #f26a1b;
    --white: #ffffff;
    --etch-silver: #9a9a9a;
    --etch-silver-dark: #6e6e6e;
  }
  * { box-sizing: border-box; margin: 0; padding: 0; }
  html, body {
    width: 1200px;
    height: 800px;
    overflow: hidden;
  }
  body {
    background: var(--canvas-bg);
    font-family: "Arimo", Arial, sans-serif;
    position: relative;
  }
  .card {
    position: absolute;
    width: 502px;
    height: 287px;
    background: var(--card-black);
  }
  .card--front { left: 45px; top: 49px; }
  .card--back  { left: 623px; top: 450px; }

  /* area reserved for the etched decoration */
  .etch-area {
    position: absolute;
    width: 36px;
    height: 94px;
    background: linear-gradient(180deg, var(--etch-silver) 0%, var(--etch-silver-dark) 100%);
    opacity: 0.55;
  }
  .card--front .etch-area { right: 18px; top: 17px; }
  .card--back .etch-area  { left: 18px; top: 17px; }

  /* brand block on front */
  .brand {
    position: absolute;
    left: 160px;
    top: 112px;
    display: flex;
    align-items: center;
    gap: 10px;
  }
  .brand__square {
    width: 22px;
    height: 22px;
    background: var(--orange);
  }
  .brand__name {
    font-weight: 700;
    font-size: 30px;
    letter-spacing: 1px;
    color: var(--orange);
    text-transform: uppercase;
    white-space: nowrap;
  }
  .tagline {
    position: absolute;
    left: 160px;
    top: 172px;
    font-size: 14.5px;
    letter-spacing: 0.3px;
    color: var(--orange);
    text-transform: uppercase;
    white-space: nowrap;
  }

  /* etched name on back */
  .etched-mark {
    position: absolute;
    left: 63px;
    top: 114px;
    width: 190px;
    padding-bottom: 8px;
    border-bottom: 2px solid var(--etch-silver-dark);
    font-weight: 700;
    font-size: 24px;
    letter-spacing: 1px;
    color: var(--etch-silver);
    text-transform: uppercase;
    white-space: nowrap;
  }

  /* contact row on back */
  .contact {
    position: absolute;
    left: 33px;
    right: 22px;
    bottom: 24px;
    display: flex;
    align-items: flex-end;
  }
  .contact__person { width: 150px; }
  .contact__name {
    color: var(--orange);
    font-size: 16px;
    text-transform: uppercase;
    letter-spacing: 0.3px;
    line-height: 1.2;
    white-space: nowrap;
  }
  .contact__role {
    color: var(--white);
    font-size: 13.5px;
    line-height: 1.3;
  }
  .contact__item {
    color: var(--orange);
    font-size: 14px;
    line-height: 1.3;
    padding-left: 14px;
    margin-left: 14px;
    border-left: 2px solid var(--white);
    white-space: nowrap;
  }
</style>
</head>
<body>

  <section class="card card--front" aria-label="Business card front">
    <div class="etch-area" role="img" aria-label="Etched decoration of dotted building columns"></div>
    <div class="brand">
      <span class="brand__square"></span>
      <span class="brand__name">Kestrel Mark</span>
    </div>
    <p class="tagline">Commercial Painting and Roofing</p>
  </section>

  <section class="card card--back" aria-label="Business card back">
    <div class="etch-area" role="img" aria-label="Etched decoration of dotted building columns"></div>
    <div class="etched-mark">Kestrel Mark</div>
    <div class="contact">
      <div class="contact__person">
        <p class="contact__name">Aled Brennan</p>
        <p class="contact__role">Director</p>
      </div>
      <p class="contact__item">aled.b@kestrelmark.com</p>
      <p class="contact__item">020 7946 0182</p>
    </div>
  </section>

</body>
</html>
```